We would like a very clean corporate, two sided business card that conveys that we are a quality focused, reliable organisation that can make a business better. We focus on a cycle of continuous improvement for IT systems.

The brief is primarily clean and corporate, nothing overly complicated.

We sell IT services, IT support, server implementation, problem solving services to businesses in Australia.

```html
<!DOCTYPE html>
<html lang="en">
<head>
<meta charset="utf-8">
<title>Northvale Systems – Business Card</title>
<link rel="stylesheet" href="https://fonts.googleapis.com/css2?family=Questrial&family=Arimo:ital,wght@0,400;1,700&display=swap">
<style>
  :root {
    --brand-crimson: #cc1142;
    --brand-ink: #2e2f3e;
    --paper: #ffffff;
    --stage: #ffffff;
    --edge: #e4e4e6;
  }
  html, body {
    margin: 0;
    padding: 0;
    width: 1200px;
    height: 900px;
    overflow: hidden;
    background: var(--stage);
  }
  .canvas {
    position: relative;
    width: 1200px;
    height: 900px;
  }
  .card {
    position: absolute;
    box-sizing: border-box;
    overflow: hidden;
  }
  .card--front {
    left: 326px;
    top: 66px;
    width: 534px;
    height: 348px;
    background: var(--brand-crimson);
  }
  .card--back {
    left: 332px;
    top: 496px;
    width: 532px;
    height: 348px;
    background: var(--paper);
    border: 1px solid var(--edge);
  }
  .wordmark {
    position: absolute;
    display: flex;
    align-items: center;
    gap: 12px;
    font-family: "Questrial", sans-serif;
    letter-spacing: -1px;
    line-height: 1;
  }
  .wordmark__dot {
    border-radius: 50%;
  }
  .card--front .wordmark {
    left: 34px;
    top: 172px;
    font-size: 64px;
    color: var(--paper);
  }
  .card--front .wordmark__dot {
    width: 34px;
    height: 34px;
    background: var(--paper);
  }
  .card--back .wordmark {
    right: 24px;
    top: 18px;
    font-size: 38px;
    color: var(--brand-ink);
  }
  .card--back .wordmark__dot {
    width: 20px;
    height: 20px;
    background: var(--brand-crimson);
  }
  .service-tag {
    position: absolute;
    right: 0;
    top: 100px;
    width: 162px;
    height: 30px;
    background: var(--brand-crimson);
    border-radius: 10px 0 0 10px;
    color: var(--paper);
    font-family: "Arimo", sans-serif;
    font-size: 19px;
    line-height: 30px;
    text-align: center;
  }
  .holder-name {
    position: absolute;
    left: 38px;
    top: 96px;
    margin: 0;
    font-family: "Questrial", sans-serif;
    font-weight: 400;
    font-size: 54px;
    color: var(--brand-crimson);
    line-height: 1;
  }
  .holder-email {
    position: absolute;
    left: 52px;
    top: 164px;
    font-family: "Arimo", sans-serif;
    font-style: italic;
    font-weight: 700;
    font-size: 16px;
    color: var(--brand-ink);
  }
  .company-details {
    position: absolute;
    right: 14px;
    top: 158px;
    margin: 0;
    font-family: "Arimo", sans-serif;
    font-style: normal;
    font-size: 14px;
    line-height: 20px;
    text-align: right;
    color: var(--brand-ink);
  }
  .company-details__contact {
    margin-top: 12px;
  }
  .web-bar {
    position: absolute;
    right: 0;
    bottom: 0;
    width: 404px;
    height: 32px;
    background: var(--brand-crimson);
    border-radius: 14px 0 0 0;
    color: var(--paper);
    font-family: "Arimo", sans-serif;
    font-size: 20px;
    letter-spacing: 5px;
    line-height: 32px;
    text-align: center;
  }
</style>
</head>
<body>
<main class="canvas">
  <section class="card card--front" aria-label="Card front">
    <div class="wordmark">
      <span>northvale</span>
      <span class="wordmark__dot"></span>
    </div>
  </section>

  <section class="card card--back" aria-label="Card back">
    <div class="wordmark">
      <span>northvale</span>
      <span class="wordmark__dot"></span>
    </div>
    <div class="service-tag">IT Services</div>

    <h1 class="holder-name">Name</h1>
    <div class="holder-email">E-mail:</div>

    <address class="company-details">
      <div>Northvale Systems Pty Ltd</div>
      <div>Suite 210, 14-18 Harbour Lane</div>
      <div>Kellerton, NSW, 2199</div>
      <div>Australia</div>
      <div class="company-details__contact">
        <div>PH: +61 2 5550 1840</div>
        <div>FAX: +61 2 5550 1841</div>
        <div>ABN: 12 345 678 901</div>
      </div>
    </address>

    <div class="web-bar">www.northvale.net</div>
  </section>
</main>
</body>
</html>
```